TruvaLink Gastronomic Social Network

Truva Link is a Gastronomic Social Network that is focused on the relationship between restaurants and customers, creating new channels to communicate with themselves and developing new tools to modernize the classic menus. In Truva Link people will see images, videos and texts related on gastronomy shared by the bests restaurants of their cities in real time. Therefore the users will feel how easy is to choose a new restaurant only few minutes before leaving their homes and how useful is to choose a meal with the images of the digital menu in order to have the best experience possible.

Target Market(s)

The direct customers of the company are the restaurants, who pay monthly to post marketing content and their digital menu. The profile of the clients will not be too restrictive: from a restaurant that offers live music and drinks to a classic and expensive restaurant.

The final users of the product are families, couples, professionals and everyone who is interested in discovering new restaurants and good gastronomy.

Requirements
Must have
• We have the idea that after the splash screen show the last registered plates from the restaurants like in pictoria story. On the story we will show the plate for the current time like lunch or dinner, a logo of the restaurant, a small description and the price.
• When selected the plate the user will be redirected to a page will restaurant details showing the selected plate as first item on restaurant menu.
• For each plate we will have a page description showing ingredients, price, harmonization and button to reserve a table.
• Reserve a table is a page for reservation.
• Also we have a page for customer info, last selected plates and restaurants.

```html
<!DOCTYPE html>
<html lang="en">
<head>
<meta charset="utf-8">
<title>Truva Link – App Screens</title>
<link href="https://fonts.googleapis.com/css2?family=Playfair+Display:wght@700&family=Lato:ital,wght@0,400;0,700;1,400&display=swap" rel="stylesheet">
<style>
  :root {
    --saffron: #e0982a;
    --plum: #4b1e3c;
    --ink: #1d1d1d;
    --muted: #b0b0b0;
    --grey: #6b6b6b;
    --white: #ffffff;
    --star: #f0a020;
    --alert: #e8423a;
  }
  * { box-sizing: border-box; margin: 0; padding: 0; }
  html, body { width: 1200px; height: 720px; overflow: hidden; background: var(--white); }
  body { position: relative; font-family: "Lato", sans-serif; color: var(--ink); }

  .backdrop-circle {
    position: absolute; left: -80px; top: -96px;
    width: 408px; height: 408px; border-radius: 50%;
    background: var(--saffron);
  }

  .screen {
    position: absolute; overflow: hidden;
    box-shadow: 0 20px 60px rgba(0,0,0,0.16);
  }
  .status {
    position: absolute; top: 0; left: 0; right: 0; height: 22px;
    display: flex; justify-content: space-between; align-items: center;
    padding: 0 14px; font-size: 7px; font-weight: 700; color: var(--white); z-index: 2;
  }
  .status svg { display: block; }

  /* Story screen */
  .story { left: 406px; top: 154px; width: 191px; height: 413px; }
  .story-photo {
    position: absolute; inset: 0;
    background:
      radial-gradient(circle at 80% 60%, rgba(110,60,45,0.85), transparent 55%),
      radial-gradient(circle at 15% 90%, rgba(150,110,40,0.8), transparent 35%),
      radial-gradient(circle at 20% 15%, rgba(120,120,90,0.7), transparent 35%),
      linear-gradient(160deg, #2b2622, #3a2a22 60%, #2a2420);
  }
  .story-shade { position: absolute; inset: 0; background: rgba(0,0,0,0.28); }
  .story-venue {
    position: absolute; left: 14px; top: 58px;
    display: flex; align-items: center; gap: 7px;
    font-size: 7.5px; font-weight: 700; color: var(--white);
  }
  .venue-dot { width: 20px; height: 20px; border-radius: 50%; background: var(--white); }
  .story-price {
    position: absolute; right: 17px; top: 54px;
    font-family: "Playfair Display", serif; font-weight: 700; font-size: 20px; color: var(--white);
  }
  .story-price sup, .dish-price sup { font-size: 0.45em; vertical-align: 0.9em; }
  .story-title {
    position: absolute; left: 13px; top: 86px;
    font-family: "Playfair Display", serif; font-weight: 700; font-size: 22px; color: var(--white);
  }
  .story-text {
    position: absolute; left: 14px; top: 121px; width: 150px;
    font-size: 7.6px; line-height: 9.6px; color: var(--white);
  }
  .story-cta {
    position: absolute; left: 13px; top: 173px; width: 81px; height: 27px;
    border: 1.5px solid var(--white); border-radius: 14px;
    display: flex; align-items: center; justify-content: center; gap: 5px;
    font-size: 7.5px; font-weight: 700; color: var(--white);
  }
  .story-thumbs { position: absolute; left: 13px; top: 322px; display: flex; gap: 4px; }
  .thumb { width: 50px; height: 38px; }
  .thumb-burger { background: linear-gradient(135deg, #b5652a, #6a3a1e); }
  .thumb-skewer { background: linear-gradient(135deg, #8a9a3a, #c8a040 55%, #3a3020); }
  .thumb-wrap { background: linear-gradient(135deg, #c77a4a, #e8d0b0 60%, #8a3a2a); }
  .story-progress {
    position: absolute; left: 12px; top: 376px; width: 162px; height: 2px;
    background: rgba(255,255,255,0.85); border-radius: 1px;
  }
  .story-chevron { position: absolute; left: 87px; top: 387px; }

  /* Dish screen */
  .dish { left: 627px; top: 50px; width: 195px; height: 620px; background: var(--white); }
  .dish-photo {
    position: absolute; left: 0; top: 0; width: 195px; height: 181px;
    background:
      radial-gradient(circle at 75% 55%, #6b3027, transparent 45%),
      radial-gradient(circle at 25% 85%, #c79a40, transparent 25%),
      radial-gradient(circle at 20% 30%, #7f9a3a, transparent 30%),
      linear-gradient(140deg, #2a2a28, #3b302b);
  }
  .dish-menu { position: absolute; left: 16px; top: 49px; }
  .dish-avatar {
    position: absolute; left: 160px; top: 45px; width: 18px; height: 18px;
    border-radius: 50%; border: 1.5px solid var(--white); background: #a08a80;
  }
  .dish-stars { position: absolute; left: 0; right: 0; top: 197px; text-align: center; font-size: 8px; letter-spacing: 2px; color: var(--star); }
  .dish-stars .off { color: #cfcfcf; }
  .dish-title {
    position: absolute; left: 0; right: 0; top: 210px; text-align: center;
    font-family: "Playfair Display", serif; font-weight: 700; font-size: 19px;
  }
  .dish-price {
    position: absolute; left: 0; right: 0; top: 235px; text-align: center;
    font-family: "Playfair Display", serif; font-weight: 700; font-size: 16px;
  }
  .dish-text {
    position: absolute; left: 20px; right: 20px; top: 265px; text-align: center;
    font-size: 6.6px; line-height: 9px; font-style: italic; color: var(--muted);
  }
  .dish-venue {
    position: absolute; left: 0; right: 0; top: 336px;
    display: flex; align-items: center; justify-content: center; gap: 6px;
    font-size: 12px; font-weight: 700; color: var(--ink);
  }
  .dish-venue-dot { width: 16px; height: 16px; border-radius: 50%; background: var(--plum); }
  .dish-venue-name { position: absolute; left: 0; right: 0; top: 370px; text-align: center; font-size: 8px; color: var(--ink); }
  .dish-venue-address { position: absolute; left: 0; right: 0; top: 381px; text-align: center; font-size: 7px; color: var(--grey); }

  .menu-row { position: absolute; top: 403px; left: -16px; display: flex; gap: 8px; }
  .menu-card { width: 82px; }
  .menu-card-photo { height: 91px; border-radius: 3px; }
  .photo-skewer { background: linear-gradient(135deg, #3a3020, #c8a040 45%, #7a9a3a); }
  .photo-burger { background: linear-gradient(160deg, #c0392b 0%, #b56a2a 35%, #6a3a1e 80%); }
  .photo-taco { background: linear-gradient(135deg, #c05a3a, #e0c090 50%, #7a3a2a); }
  .menu-card-title { margin-top: 8px; font-family: "Playfair Display", serif; font-weight: 700; font-size: 7.5px; white-space: nowrap; }
  .menu-card-text { margin-top: 4px; font-size: 6px; line-height: 8px; font-style: italic; color: var(--muted); }

  .tab-bar {
    position: absolute; left: 0; bottom: 0; width: 195px; height: 66px; background: var(--plum);
    display: flex; justify-content: space-around; padding: 14px 6px 0;
  }
  .tab { display: flex; flex-direction: column; align-items: center; gap: 4px; font-size: 5.5px; color: #d8c8d2; width: 40px; position: relative; }
  .tab-active { color: var(--saffron); }
  .tab-badge { position: absolute; top: -1px; left: 24px; width: 4px; height: 4px; border-radius: 50%; background: var(--alert); }
  .home-indicator { position: absolute; left: 62px; bottom: 8px; width: 72px; height: 2.5px; border-radius: 2px; background: #1a0a14; }

  /* Splash screen */
  .splash { left: 859px; top: 137px; width: 195px; height: 448px; background: var(--saffron); }
  .splash-mark { position: absolute; left: 89px; top: 200px; width: 18px; height: 18px; border-radius: 50%; background: var(--plum); }
  .splash-name {
    position: absolute; left: 0; right: 0; top: 230px; text-align: center;
    font-size: 15px; color: var(--plum);
  }
</style>
</head>
<body>

<div class="backdrop-circle"></div>

<!-- Story screen -->
<section class="screen story">
  <div class="story-photo" role="img" aria-label="Close-up photo of sliced lamb steak with vegetables and pepper sauce"></div>
  <div class="story-shade"></div>
  <div class="status">
    <span>9:41</span>
    <svg width="34" height="7" viewBox="0 0 34 7" fill="#fff"><rect x="0" y="4" width="1.5" height="3"/><rect x="2.5" y="3" width="1.5" height="4"/><rect x="5" y="1.5" width="1.5" height="5.5"/><rect x="7.5" y="0" width="1.5" height="7"/><path d="M13 3a5 5 0 0 1 7 0l-1 1a3.5 3.5 0 0 0-5 0z M15 5a2 2 0 0 1 3 0l-1.5 1.5z"/><rect x="24" y="1" width="8" height="5" rx="1"/></svg>
  </div>
  <div class="story-venue"><span class="venue-dot"></span>Vela Resto Bar</div>
  <div class="story-price"><sup>$</sup>99</div>
  <h1 class="story-title">Lamb Steak</h1>
  <p class="story-text">Lorem ipsum dolor sit amet, consectetur adipisicing elit, sed do eiusmod tempor incididunt ut labore et dolore magna aliqua. Ut enim ad minim veniam,</p>
  <div class="story-cta">I want this
    <svg width="9" height="6" viewBox="0 0 9 6" fill="none" stroke="#fff" stroke-width="0.9"><path d="M0 3h8M5.5 0.5L8 3 5.5 5.5"/></svg>
  </div>
  <div class="story-thumbs">
    <div class="thumb thumb-burger" role="img" aria-label="Burger photo"></div>
    <div class="thumb thumb-skewer" role="img" aria-label="Skewers photo"></div>
    <div class="thumb thumb-wrap" role="img" aria-label="Wrap photo"></div>
  </div>
  <div class="story-progress"></div>
  <svg class="story-chevron" width="16" height="9" viewBox="0 0 16 9" fill="none" stroke="#fff" stroke-width="1.4"><path d="M1 8L8 1l7 7"/></svg>
</section>

<!-- Dish detail screen -->
<section class="screen dish">
  <div class="dish-photo" role="img" aria-label="Top-down photo of lamb steak with vegetables and sauce"></div>
  <div class="status">
    <span>9:41</span>
    <svg width="34" height="7" viewBox="0 0 34 7" fill="#fff"><rect x="0" y="4" width="1.5" height="3"/><rect x="2.5" y="3" width="1.5" height="4"/><rect x="5" y="1.5" width="1.5" height="5.5"/><rect x="7.5" y="0" width="1.5" height="7"/><path d="M13 3a5 5 0 0 1 7 0l-1 1a3.5 3.5 0 0 0-5 0z M15 5a2 2 0 0 1 3 0l-1.5 1.5z"/><rect x="24" y="1" width="8" height="5" rx="1"/></svg>
  </div>
  <svg class="dish-menu" width="11" height="9" viewBox="0 0 11 9" stroke="#fff" stroke-width="1.2"><path d="M0 1h11M0 4.5h11M0 8h7"/></svg>
  <div class="dish-avatar" role="img" aria-label="User profile photo"></div>

  <div class="dish-stars">★★★★<span class="off">★</span></div>
  <h2 class="dish-title">Lamb Steak</h2>
  <div class="dish-price"><sup>$</sup>99</div>
  <p class="dish-text">Gumbo beet greens corn soko endive gumbo gourd. Parsley shallot courgette tatsoi pea sprouts fava bean collard greens dandelion okra wakame tomato. Dandelion cucumber earthnut pea peanut soko zucchini.</p>

  <div class="dish-venue"><span class="dish-venue-dot"></span>Vela</div>
  <div class="dish-venue-name">Vela Resto Bar</div>
  <div class="dish-venue-address">112 Olive St. Fennel Ave.</div>

  <div class="menu-row">
    <article class="menu-card">
      <div class="menu-card-photo photo-skewer" role="img" aria-label="Grilled skewers photo"></div>
      <h3 class="menu-card-title">Skwers</h3>
      <p class="menu-card-text">Gumbo beet greens corn soko endive gumbo</p>
    </article>
    <article class="menu-card">
      <div class="menu-card-photo photo-burger" role="img" aria-label="Burger photo"></div>
      <h3 class="menu-card-title">Burger Supreme</h3>
      <p class="menu-card-text">Gumbo beet greens corn soko endive gumbo</p>
    </article>
    <article class="menu-card">
      <div class="menu-card-photo photo-taco" role="img" aria-label="Tacos photo"></div>
      <h3 class="menu-card-title">Taco's &amp; Wraps</h3>
      <p class="menu-card-text">Gumbo beet greens corn soko endive gumbo</p>
    </article>
  </div>

  <nav class="tab-bar">
    <div class="tab">
      <svg width="12" height="12" viewBox="0 0 12 12" fill="none" stroke="#d8c8d2" stroke-width="0.9"><path d="M1 6L6 1.5 11 6M2.5 5v6h7V5M5 11V8h2v3"/></svg>HOME
    </div>
    <div class="tab tab-active">
      <span class="tab-badge"></span>
      <svg width="12" height="12" viewBox="0 0 12 12" fill="none" stroke="#e0982a" stroke-width="0.9"><path d="M6 11.5S2 7.5 2 4.8a4 4 0 0 1 8 0C10 7.5 6 11.5 6 11.5z"/><circle cx="6" cy="4.8" r="1.4"/></svg>PLACES
    </div>
    <div class="tab">
      <svg width="12" height="12" viewBox="0 0 12 12" fill="none" stroke="#d8c8d2" stroke-width="0.9"><path d="M2.5 9V5.5a3.5 3.5 0 0 1 7 0V9l1 1H1.5zM5 11h2M6 1v1"/></svg>MAPS
    </div>
    <div class="tab">
      <svg width="12" height="12" viewBox="0 0 12 12" fill="none" stroke="#d8c8d2" stroke-width="0.9"><circle cx="6" cy="6" r="5"/><path d="M6 5.5v3M6 3.5v.6"/></svg>HOW TO
    </div>
  </nav>
  <div class="home-indicator"></div>
</section>

<!-- Splash screen -->
<section class="screen splash">
  <div class="status">
    <span>9:41</span>
    <svg width="34" height="7" viewBox="0 0 34 7" fill="#fff"><rect x="0" y="4" width="1.5" height="3"/><rect x="2.5" y="3" width="1.5" height="4"/><rect x="5" y="1.5" width="1.5" height="5.5"/><rect x="7.5" y="0" width="1.5" height="7"/><path d="M13 3a5 5 0 0 1 7 0l-1 1a3.5 3.5 0 0 0-5 0z M15 5a2 2 0 0 1 3 0l-1.5 1.5z"/><rect x="24" y="1" width="8" height="5" rx="1"/></svg>
  </div>
  <span class="splash-mark"></span>
  <div class="splash-name">Truva Link</div>
</section>

</body>
</html>
```